Build a landing page to promote a service (dialler consultation and support).

We are a call centre consultation firm and we need a landing page to promote a service. The service is Mornatex dialler consultation and support.
If you do not know what Mornatex is, please do some quick "Zorpli" research for more information.
The landing page will be promoted with a paid advertisement, so we want something that is simple, and explains exactly what service we offer.
There are two objectives for the landing page:
1) A "call to action" which directs the user to a contact page, including a form plus all of our contact details.
2) A form for them viewers to enter their details to get a "FREE" quote for their project. This form should be placed on the main page.
Notes:
The call to action will require the viewer to enter their name, email, phone number as well as a description of their request. There will also need to be a drop down menu for the type of quote. This menu should have the following options:
1) Mornatex support
2) Mornatex hosting
3) Mornatex customisation
4) Other
We need 2 pages in total:
1) Main landing page
This is the home page. It will need to clearly indicate our services and our key selling features.
Services:
* Mornatex support
* Mornatex hosting
* Mornatex customisation
Key Selling Features:
* Australian based
* PCI complaint
* 10+ years of dialler and call centre experience
* we run a sister company which is a highly reputable 40 seat call centre, so we know first hand about call centre technology.
The main landing page will have an "about us" section with a few paragraphs about how we got started.
-------------------------------------------------------------------------
2) Contact page
All of our contact details will live on this page, as well as a contact form.
Other notes:
We will be self hosting the landing page.
We already have a domain name.
The design must be clean and incorporate our logo, as well as it's colours. (Logo attached)
We want a fully function HTML landing page, not just a "PSD" design.
The page must be mobile optimised.
Anyone using Mornatex software.

```html
<!DOCTYPE html>
<html lang="en">
<head>
<meta charset="utf-8">
<title>Contact us – Callvane</title>
<link rel="stylesheet" href="https://fonts.googleapis.com/css2?family=Poppins:wght@400;500&family=Open+Sans:wght@400;600&display=swap">
<style>
:root{
  --teal:#2aa89a;
  --blue:#1e7fc9;
  --ink:#1c1c1c;
  --text:#555;
  --form-bg:#e9f7fc;
  --form-border:#b9c9d3;
  --footer:#111111;
  --footer-base:#0a0a0a;
  --white:#ffffff;
}
*{margin:0;padding:0;box-sizing:border-box}
html,body{width:810px;height:1200px;overflow:hidden;background:var(--white)}
body{position:relative;font-family:"Open Sans",sans-serif;color:var(--ink)}
.abs{position:absolute}

.top-rule{left:0;top:0;width:810px;height:3px;background:var(--teal)}
.brand{display:flex;align-items:center;gap:6px}
.brand-dot{border-radius:50%;background:var(--blue)}
.brand-name{font-family:"Poppins",sans-serif;font-weight:500;color:var(--blue)}
.site-header .brand{left:60px;top:18px}
.site-header .brand-dot{width:26px;height:26px}
.site-header .brand-name{font-size:17px}
.nav{top:27px;right:62px;display:flex;gap:23px;font-family:"Poppins",sans-serif;font-size:12px;color:var(--ink)}
.nav .active{color:var(--blue)}

.hero{left:0;top:74px;width:810px;height:154px}
.hero-title{left:0;top:114px;width:810px;text-align:center;font-family:"Poppins",sans-serif;font-weight:500;font-size:33px;color:var(--white)}

.intro{left:60px;top:307px;width:690px;font-size:10.4px;line-height:18.4px;color:var(--text)}

.contact-form{left:60px;top:423px;width:373px;height:389px;background:var(--form-bg);border:1px solid var(--form-border)}
.form-title{position:absolute;left:40px;top:16px;font-family:"Poppins",sans-serif;font-size:17px}
.field{position:absolute;left:36px;width:300px;height:43px;background:var(--white);border:1px solid #8a8f94;border-radius:2px;font-family:"Poppins",sans-serif;font-size:11px;padding:14px 11px;color:#222}
.field.focus{border-color:#7c9bb8;box-shadow:0 3px 8px rgba(0,0,0,.18)}
.field.message{height:89px}
.submit{position:absolute;left:113px;top:332px;width:146px;height:34px;border-radius:17px;background:linear-gradient(90deg,var(--teal),var(--blue));color:var(--white);font-family:"Poppins",sans-serif;font-size:15px;text-align:center;line-height:34px;box-shadow:0 8px 12px rgba(42,168,154,.25)}

.info-item{left:480px;width:280px;height:60px}
.info-item svg{position:absolute;left:0;top:0}
.info-label{position:absolute;left:71px;top:0;font-size:12px;color:var(--ink)}
.info-text{position:absolute;left:71px;top:18px;font-size:11.2px;line-height:17px;color:#444}

.map{left:471px;top:654px;width:280px;height:158px;background:linear-gradient(135deg,#e4e4e4,#cfcfcf);border:1px solid #bbb}

.footer-band{left:0;top:880px;width:810px;height:320px}
.footer-base{left:0;top:1152px;width:810px;height:48px;background:var(--footer-base)}
.site-footer .brand{left:70px;top:1010px}
.site-footer .brand-dot{width:40px;height:40px}
.site-footer .brand-name{font-size:24px}
.col-title{font-size:14.4px;color:var(--white);top:987px}
.contact-line{left:288px;font-size:11px;color:var(--white)}
.contact-line b{font-weight:600;display:block;font-size:11px}
.contact-line span{font-size:10px}
.links{top:1017px;list-style:none;font-size:11px;line-height:22.6px;color:var(--white)}
.copyright{left:0;top:1168px;width:810px;text-align:center;font-size:10px;color:#aaa}
</style>
</head>
<body>

<div class="abs top-rule"></div>

<header class="site-header">
  <div class="abs brand"><span class="brand-dot"></span><span class="brand-name">Callvane</span></div>
  <nav class="abs nav">
    <span>Home</span><span>About us</span><span>Services</span><span>Products</span><span>News</span><span class="active">Contact us</span>
  </nav>
</header>

<svg class="abs hero" viewBox="0 0 810 154" role="img" aria-label="Banner photo of call centre agents wearing headsets, tinted teal to blue">
  <defs>
    <linearGradient id="heroTint" x1="0" y1="0" x2="1" y2="0">
      <stop offset="0" stop-color="#2a9b93"/>
      <stop offset="1" stop-color="#1f77b8"/>
    </linearGradient>
  </defs>
  <polygon points="0,0 810,0 810,154 0,98" fill="url(#heroTint)"/>
</svg>
<h1 class="abs hero-title">Contact us</h1>

<p class="abs intro">It is a long established fact that a reader will be distracted by the readable content of a page when looking at its layout. The point of using Lorem Ipsum is that it has a more-or-less normal distribution of letters, as opposed to using 'Content here, content here', making it look like readable English. Many desktop publishing packages and web page editors now use Lorem Ipsum as their default model text, and a search for</p>

<section class="abs contact-form">
  <h2 class="form-title">Contact Form</h2>
  <div class="field focus" style="top:61px">Name</div>
  <div class="field" style="top:115px">Email id</div>
  <div class="field" style="top:169px">Phone</div>
  <div class="field message" style="top:223px">Message</div>
  <div class="submit">Submit</div>
</section>

<div class="abs info-item" style="top:433px">
  <svg width="40" height="34" viewBox="0 0 40 34"><rect x="2" y="3" width="36" height="27" rx="2" fill="none" stroke="var(--teal)" stroke-width="1.6"/><polyline points="2,5 20,19 38,5" fill="none" stroke="var(--blue)" stroke-width="1.6"/></svg>
  <div class="info-label">Email</div>
  <div class="info-text">info@callvane-mail.com</div>
</div>

<div class="abs info-item" style="top:493px">
  <svg width="40" height="44" viewBox="0 0 40 44"><rect x="8" y="7" width="24" height="36" rx="3" fill="none" stroke="var(--teal)" stroke-width="1.6"/><line x1="8" y1="13" x2="32" y2="13" stroke="var(--blue)" stroke-width="1.4"/><line x1="8" y1="36" x2="32" y2="36" stroke="var(--blue)" stroke-width="1.4"/><line x1="17" y1="40" x2="23" y2="40" stroke="var(--blue)" stroke-width="1.4"/></svg>
  <div class="info-label">Call Us !</div>
  <div class="info-text">+123 456 7890<br>+123 456 7890</div>
</div>

<div class="abs info-item" style="top:573px">
  <svg width="40" height="44" viewBox="0 0 40 44"><path d="M20 30 C12 20 11 15 11 12 a9 9 0 0 1 18 0 c0 3-1 8-9 18z" fill="none" stroke="var(--blue)" stroke-width="1.6"/><circle cx="20" cy="12" r="3.5" fill="none" stroke="var(--blue)" stroke-width="1.4"/><polyline points="12,26 3,42 13,38 20,42 27,38 37,42 28,26" fill="none" stroke="var(--teal)" stroke-width="1.6"/></svg>
  <div class="info-label">Address</div>
  <div class="info-text">123, Main Road, New City,<br>My Country 123456</div>
</div>

<div class="abs map" role="img" aria-label="Street map with a red location pin marking the office"></div>

<svg class="abs footer-band" viewBox="0 0 810 320" preserveAspectRatio="none">
  <defs>
    <linearGradient id="bandTint" x1="0" y1="0" x2="1" y2="0">
      <stop offset="0" stop-color="var(--teal)"/>
      <stop offset="1" stop-color="var(--blue)"/>
    </linearGradient>
  </defs>
  <polygon points="0,8 810,50 810,320 0,320" fill="url(#bandTint)"/>
  <polygon points="0,18 810,66 810,320 0,320" fill="var(--footer)"/>
</svg>
<div class="abs footer-base"></div>

<footer class="site-footer">
  <div class="abs brand"><span class="brand-dot"></span><span class="brand-name">Callvane</span></div>

  <div class="abs col-title" style="left:288px">CONTACT US</div>
  <div class="abs contact-line" style="top:1020px">
    <svg class="abs" style="left:0;top:3px" width="14" height="11" viewBox="0 0 14 11"><rect x="0.6" y="0.6" width="12.8" height="9.8" fill="none" stroke="#fff" stroke-width="1"/><polyline points="0.6,1 7,6 13.4,1" fill="none" stroke="#fff" stroke-width="1"/></svg>
    <div style="margin-left:19px"><b>EMAIL ADDRESS</b><span>info@callvane-mail.com</span></div>
  </div>
  <div class="abs contact-line" style="top:1065px">
    <svg class="abs" style="left:0;top:4px" width="14" height="14" viewBox="0 0 14 14"><path d="M3 1 L5 4 L4 6 C5 8 6 9 8 10 L10 9 L13 11 L11 13 C6 12 2 8 1 3z" fill="none" stroke="#fff" stroke-width="1"/></svg>
    <div style="margin-left:19px"><b>PHONE NUMBER</b><span>(555) 010-4818</span></div>
  </div>

  <div class="abs col-title" style="left:494px">ABOUT</div>
  <ul class="abs links" style="left:494px"><li>Home</li><li>About Us</li><li>Services</li><li>Products</li></ul>

  <div class="abs col-title" style="left:650px">RESOURCES</div>
  <ul class="abs links" style="left:652px"><li>News</li><li>Support</li><li>Faq</li><li>Contact</li></ul>

  <p class="abs copyright">© 2018 Company Name&nbsp; All right reserved</p>
</footer>

</body>
</html>
```